Banner (html, flash, gifs, jpgs or html5) - TwinOrbits

We need horizontal banners and copy created that would get people to click for holiday purposes that will go here: https://www.twinorbitsdemo.com/blog.htm
The specs on the rich media unit ads are:
•	Audience - lifestyle interest, 18-35 age group
•	Multiple calls to action offer opportunities to further engage
•	Unit dimensions are 800x80
•	Max file size 1 MB
•	We can take html, flash, gifs, jpgs or html5
Please include a thumbnail image for 2 of the 3 options below:
1) a thumbnail image for Free Sign Up - https://www.twinorbitsdemo.com/ppcRegistration2.htm
2) a thumbnail image for Astrology Reports - astrology.twinorbitsdemo.com
3) a thumbnail image for iOS and Android app
and
Include a coupon code respective of the holiday you choose:
Promo	Day	Holiday
NewYou	1/1	New Year's Day
Dream	1/18	Martin Luther King, Jr. Day
BeMine	2/14	Valentines Day
PresDay	2/15	Presidents Day
NewLove	3/27	Spring
ForHer	5/8	Mothers Day
MDUSA	5/30	Memorial Day
ForHim	6/19	Fathers day
Fireworks	7/4	Independence Day
Passion	8/1	Summer Love
Fall4U	10/10	Columbus Day
Treat	10/31	Halloween
ThankYou	11/24	Thanksgiving Day
Snuggle	12/25	Happy Holidays
Twin Orbits–
Here is a little about the company - www.twinorbitsdemo.com, https://www.twinorbitsdemo.com/ppcRegistration2.htm

Look and feel
Each slider illustrates characteristics of the customer's brand and the style your logo design should communicate.

```html
<!DOCTYPE html>
<html lang="en">
<head>
<meta charset="utf-8">
<title>TwinOrbits Holiday Banner</title>
<link href="https://fonts.googleapis.com/css2?family=Caveat+Brush&family=Open+Sans:wght@600&display=swap" rel="stylesheet">
<style>
  :root {
    --white: #ffffff;
    --ink: #111111;
    --wave-blue: #2f8fd8;
    --wave-light: #bfe0f7;
    --brush-navy: #1d3f8c;
    --sky-top: #cfe4f2;
    --hill-green: #6f9f74;
    --sea-turquoise: #3cc3d6;
    --sand: #f1ead8;
  }
  * { margin: 0; padding: 0; box-sizing: border-box; }
  html, body { width: 1200px; height: 120px; overflow: hidden; background: var(--white); }
  .banner { position: relative; width: 1200px; height: 120px; overflow: hidden; background: var(--white); }
  .photo { position: absolute; top: 0; height: 120px; }
  .photo--travellers {
    left: 0; width: 500px;
    background: linear-gradient(180deg, var(--sky-top) 0%, #b7d3e3 40%, var(--hill-green) 75%, #4d7a57 100%);
  }
  .photo--beach {
    left: 868px; width: 332px;
    background: linear-gradient(180deg, #7cc4ee 0%, #aee0f3 40%, var(--sea-turquoise) 62%, var(--sand) 78%, #e7dcc2 100%);
  }
  .shapes { position: absolute; inset: 0; }
  .tag {
    position: absolute;
    font-family: "Caveat Brush", cursive;
    font-size: 32px;
    line-height: 1;
    white-space: nowrap;
  }
  .tag--holidays { left: 252px; top: 14px; color: var(--ink); transform: rotate(-7deg); }
  .tag--coupons {
    left: 552px; top: 20px; color: var(--white); font-size: 31px; transform: rotate(-6deg);
    -webkit-text-stroke: 1px var(--ink);
  }
  .tag--locations { left: 948px; top: 46px; color: var(--ink); transform: rotate(-7deg); }
  .promo-code {
    position: absolute; left: 612px; top: 58px;
    font-family: "Open Sans", sans-serif; font-weight: 600; font-size: 33px;
    color: var(--ink); letter-spacing: 0.3px;
  }
</style>
</head>
<body>
<main class="banner">
  <div class="photo photo--travellers" role="img" aria-label="Young couple with backpacks taking a photo above a green mountain valley"></div>
  <div class="photo photo--beach" role="img" aria-label="Tropical beach with parasol, sun loungers, palm leaves and turquoise sea"></div>

  <svg class="shapes" width="1200" height="120" viewBox="0 0 1200 120" aria-hidden="true">
    <!-- blue wave dividing the left photo from the coupon panel -->
    <path d="M470 0 H840 C760 22 640 10 560 40 C520 56 500 90 505 120 H480 C470 80 460 40 470 0 Z" fill="var(--wave-blue)"/>
    <path d="M540 0 H820 C740 16 650 14 590 30 C560 38 548 30 540 0 Z" fill="var(--wave-light)"/>
    <!-- white brush under "Excited Holidays" -->
    <path d="M232 44 C300 20 400 6 488 2 L492 18 C420 26 330 40 246 62 Z" fill="var(--white)"/>
    <path d="M240 30 C320 12 410 4 470 4 L472 10 C400 14 320 24 244 40 Z" fill="var(--white)"/>
    <!-- navy brush under "Special Coupons" -->
    <path d="M530 52 C600 28 690 14 760 12 L758 36 C690 40 610 52 538 66 Z" fill="var(--brush-navy)"/>
    <!-- white brush under "Excited Locations" -->
    <path d="M922 80 C990 56 1090 40 1172 40 L1168 62 C1090 66 1000 82 930 94 Z" fill="var(--white)"/>
    <path d="M930 66 C1000 48 1090 38 1160 38 L1160 46 C1090 48 1010 58 934 74 Z" fill="var(--white)"/>
  </svg>

  <p class="tag tag--holidays">Excited Holidays</p>
  <p class="tag tag--coupons">Special Coupons</p>
  <p class="promo-code">#NewYou</p>
  <p class="tag tag--locations">Excited Locations</p>
</main>
</body>
</html>
```